Poster Design with Yoga Foam Roller Exercise Guide

Hi there!
We are looking for a poster design for our yoga foam roller product.
1. Foam roller.jpg shows our product. The poster is going to be wrapped around the roller
2. Poster dimensions: 42x28.5cm.
3. Design style matches our reference box.png and reference flat.png (colors, typefaces, overall look & feel)
4. Also check reference poster.jpg as a reference design for use of colors and overall look & feel
5. Written instructions are to be taken from written instructions.pdf
6. Illustrations are to be taken from illustrations.zip
7. Also use illustrations #2, 3 and 8 from girls.jpg, but add faces and change girl's hair (according to hair.jpg)
8. please see "orchard pals. jpg" for the ambience of the colours (instead of green, please use a brown colour). the base colours must be plain, without grain.
9. Please also create a small label design (53x17mm, to be inserted into a socket in the foam roller, see label.jpg). Please use our logo (reference box/reference flat/logo.jpg) and/or „Velvet Harbor“ as text as you see fit.
Thank you very much, we are really excited about receiving your designs :)

```html
<!DOCTYPE html>
<html lang="en">
<head>
<meta charset="utf-8">
<title>Velvet Harbor – Faszienrolle</title>
<link rel="stylesheet" href="https://fonts.googleapis.com/css2?family=Raleway:wght@300;400&family=Roboto+Condensed:wght@400;700&display=swap">
<style>
  :root {
    --page: #ffffff;
    --brown: #8b6a4b;
    --brown-dark: #7a5b3e;
    --sand: #ede1d2;
    --cream: #f6ecdf;
    --heading: #7c5634;
    --body: #3d3a37;
    --figure: #d9c9b6;
  }
  * { margin: 0; padding: 0; box-sizing: border-box; }
  html, body { width: 1200px; height: 978px; overflow: hidden; background: var(--page); }
  body { position: relative; font-family: "Roboto Condensed", sans-serif; }

  .poster { position: absolute; left: 34px; top: 40px; width: 1132px; height: 768px; background: var(--sand); overflow: hidden; }
  .poster-panel { position: absolute; left: 0; top: 0; }

  .brand { position: absolute; left: 0; width: 332px; text-align: center; color: var(--cream); }
  .brand-name { top: 218px; font-family: "Raleway", sans-serif; font-weight: 400; font-size: 15px; letter-spacing: 5px; }
  .brand-dot { position: absolute; left: 150px; top: 130px; width: 32px; height: 32px; border-radius: 50%; background: var(--cream); }
  .product-title { top: 306px; font-family: "Raleway", sans-serif; font-weight: 300; font-size: 43px; }
  .product-variant { top: 366px; font-family: "Raleway", sans-serif; font-style: italic; font-weight: 300; font-size: 17px; }
  .figure-seated { position: absolute; left: 70px; top: 418px; width: 196px; height: 206px; background: var(--cream); border-radius: 48% 48% 40% 40% / 30% 30% 60% 60%; }
  .website { top: 674px; font-family: "Raleway", sans-serif; font-size: 16px; }

  .exercise-figure { position: absolute; background: linear-gradient(90deg, #e8a05a, #c9bfb4); opacity: .55; border-radius: 6px; }
  .exercise { position: absolute; width: 170px; }
  .exercise h2 { font-size: 10px; font-weight: 700; color: var(--heading); text-transform: uppercase; letter-spacing: .2px; margin-bottom: 1px; }
  .exercise p { font-size: 8.6px; line-height: 11.2px; color: var(--body); }
  .exercise.narrow { width: 118px; }
  .exercise.wide { width: 280px; }
  .divider { position: absolute; width: 1px; background: #cbb9a5; }
  .faint-dot { position: absolute; left: 1000px; top: 640px; width: 80px; height: 80px; border-radius: 50%; border: 2px solid #dccbb7; }

  .label { position: absolute; top: 847px; width: 280px; height: 89px; background: var(--brown); }
  .label::after { content: ""; position: absolute; inset: 4px; border: 1px solid #b59a7e; }
  .label-brand { position: absolute; left: 18px; top: 56px; width: 120px; text-align: center; font-family: "Raleway", sans-serif; font-size: 7.5px; letter-spacing: 2.5px; color: var(--cream); }
  .label-dot { position: absolute; left: 70px; top: 22px; width: 16px; height: 16px; border-radius: 50%; background: var(--cream); }
  .label-title { position: absolute; left: 135px; top: 30px; font-family: "Raleway", sans-serif; font-weight: 300; font-size: 22px; color: var(--cream); }
  .label-variant { position: absolute; left: 170px; top: 58px; font-family: "Raleway", sans-serif; font-style: italic; font-size: 8px; color: var(--cream); }
</style>
</head>
<body>
  <section class="poster">
    <svg class="poster-panel" width="1132" height="768" viewBox="0 0 1132 768">
      <path d="M0 0 L238 0 Q430 384 262 768 L0 768 Z" fill="var(--brown)"/>
      <path d="M218 0 Q410 384 242 768" fill="none" stroke="#b39a80" stroke-width="1"/>
      <path d="M250 0 Q442 384 274 768" fill="none" stroke="#ffffff" stroke-opacity=".5" stroke-width="1"/>
    </svg>

    <div class="brand-dot"></div>
    <div class="brand brand-name">VELVET HARBOR</div>
    <div class="brand product-title">Faszienrolle</div>
    <div class="brand product-variant">schwarz/blau</div>
    <div class="figure-seated" role="img" aria-label="Silhouette of a woman sitting cross-legged in meditation"></div>
    <div class="brand website">www.velvetharbor.com</div>

    <div class="exercise-figure" style="left:438px;top:52px;width:170px;height:104px" role="img" aria-label="Man rolling calves on a foam roller"></div>
    <div class="exercise" style="left:441px;top:175px"><h2>Calves</h2><p>Lorem Ipsum is simply dummy text of the printing and typesetting industry. Lorem Ipsum has been the industry's standard dummy text ever since the 1500s,</p></div>

    <div class="exercise-figure" style="left:670px;top:52px;width:170px;height:104px" role="img" aria-label="Man rolling back of upper thighs on a foam roller"></div>
    <div class="exercise" style="left:670px;top:175px"><h2>Back upper thighs</h2><p>Lorem Ipsum is simply dummy text of the printing and typesetting industry. Lorem Ipsum has been the industry's standard dummy text ever since the 1500s,</p></div>

    <div class="exercise-figure" style="left:892px;top:92px;width:204px;height:62px" role="img" aria-label="Man lying on his side rolling lateral back"></div>
    <div class="exercise" style="left:902px;top:175px"><h2>Lateral back</h2><p>Lorem Ipsum is simply dummy text of the printing and typesetting industry. Lorem Ipsum has been the industry's standard dummy text ever since the 1500s,</p></div>

    <div class="exercise-figure" style="left:438px;top:260px;width:170px;height:104px" role="img" aria-label="Man rolling buttock on a foam roller"></div>
    <div class="exercise" style="left:441px;top:380px"><h2>Buttock</h2><p>Lorem Ipsum is simply dummy text of the printing and typesetting industry. Lorem Ipsum has been the industry's standard dummy text ever since the 1500s,</p></div>

    <div class="exercise-figure" style="left:660px;top:292px;width:200px;height:72px" role="img" aria-label="Man on forearms rolling inside of upper thigh"></div>
    <div class="exercise" style="left:670px;top:380px"><h2>Inside of upper thighs</h2><p>Lorem Ipsum is simply dummy text of the printing and typesetting industry. Lorem Ipsum has been the industry's standard dummy text ever since the 1500s,</p></div>

    <div class="exercise-figure" style="left:910px;top:266px;width:64px;height:160px" role="img" aria-label="Man standing against a wall rolling upper back"></div>
    <div class="divider" style="left:975px;top:260px;height:180px"></div>
    <div class="exercise narrow" style="left:986px;top:336px"><h2>Upper back</h2><p>Lorem Ipsum is simply dummy text of the printing and typesetting industry. Lorem Ipsum has been the industry's standard dummy text ever since the 1500s,</p></div>

    <div class="exercise-figure" style="left:436px;top:478px;width:172px;height:74px" role="img" aria-label="Woman lying on foam roller rolling upper back"></div>
    <div class="exercise" style="left:441px;top:568px"><h2>Uppar back</h2><p>Lorem Ipsum is simply dummy text of the printing and typesetting industry. Lorem Ipsum has been the industry's standard dummy text ever since the 1500s,</p></div>

    <div class="exercise-figure" style="left:654px;top:472px;width:200px;height:80px" role="img" aria-label="Woman rolling front of upper thigh on a foam roller"></div>
    <div class="exercise" style="left:670px;top:568px"><h2>Front of uppar thighs</h2><p>Lorem Ipsum is simply dummy text of the printing and typesetting industry. Lorem Ipsum has been the industry's standard dummy text ever since the 1500s,</p></div>

    <div class="exercise-figure" style="left:904px;top:448px;width:72px;height:174px" role="img" aria-label="Man standing with foam roller at shoulder against a wall"></div>
    <div class="divider" style="left:975px;top:450px;height:170px"></div>
    <div class="exercise narrow" style="left:986px;top:516px"><h2>Shoulder standing</h2><p>Lorem Ipsum is simply dummy text of the printing and typesetting industry. Lorem Ipsum has been the industry's standard dummy text ever since the 1500s,</p></div>

    <div class="exercise-figure" style="left:422px;top:652px;width:200px;height:66px" role="img" aria-label="Woman lying face down rolling inside thighs"></div>
    <div class="exercise wide" style="left:671px;top:675px"><h2>Inside thighs</h2><p>Lorem Ipsum is simply dummy text of the printing and typesetting industry. Lorem Ipsum has been the industry's standard dummy text ever since the 1500s,</p></div>

    <div class="faint-dot"></div>
  </section>

  <div class="label" style="left:320px">
    <div class="label-dot"></div>
    <div class="label-brand">VELVET HARBOR</div>
    <div class="label-title">Faszienrolle</div>
    <div class="label-variant">schwarz/blau</div>
  </div>
  <div class="label" style="left:619px">
    <div class="label-dot"></div>
    <div class="label-brand">VELVET HARBOR</div>
    <div class="label-title">Faszienrolle</div>
    <div class="label-variant">schwarz/blau</div>
  </div>
</body>
</html>
```